Red Lantern Take Away, take away menu

We want to use the double sided flyer design to produce a bulk amount of take away menus, which incorporate full contact details for our two shopfronts. We are a Take Away business in Wagga Wagga NSW, with two store, one which opened last year. We may also look to use these flyers for a letter box drop into the future. Our detailed menu can be found at redlanterntakeaway.com.au and contact details for both shops can be found on our facebook page Red Lantern Take Away.
Updates

Hi all, Please note that the menu prices on our website are not the current prices. Please contact me with an email so I can send through a correct copy. I will be extending the due date to compensate for this oversight. Thanks.

Reason: Deadline is being extended as the old prices are still advertised on our menu (@redlanterntakeaway.com) . Please contact me via email for a copy of the up to date pricing.

Hi all, Please note that a file has been updated to the brief with current pricing. Please use this pricing in any proposals. Please don't use any of the combo deals in your proposals as they may be subject to change. Please also have a disclaimer at the bottom of your flyer that states "Please note: Prices may be subject to change". Sorry about the dripping of information as this is our first time using sketch forge. Thanks.

Industry/Entity Type

Business

```html
<!DOCTYPE html>
<html lang="en">
<head>
<meta charset="utf-8">
<title>Red Lantern Take Away – Menu Flyer</title>
<link rel="stylesheet" href="https://fonts.googleapis.com/css2?family=Arimo&family=Cinzel&family=Poiret+One&family=Satisfy&display=swap">
<style>
  :root {
    --page: #e4e4e6;
    --wood-dark: #4a2c17;
    --wood-mid: #7a4a26;
    --wood-light: #a06a3c;
    --sun-gold: #f2a930;
    --sun-deep: #d9781e;
    --sea: #2e3d52;
    --brand-blue: #1d5aa6;
    --brand-blue-dark: #164684;
    --panel: rgba(246, 229, 208, 0.9);
    --panel-edge: #8793a3;
    --ink: #2b2b2b;
    --label: #ffffff;
    --logo-ink: #1d5aa6;
  }
  * { box-sizing: border-box; margin: 0; padding: 0; }
  html, body { width: 1200px; height: 849px; overflow: hidden; background: var(--page); }
  .canvas { position: relative; width: 1200px; height: 849px; }

  .flyer {
    position: absolute; top: 40px; width: 500px; height: 770px; overflow: hidden;
    box-shadow: 0 8px 22px rgba(0,0,0,.25);
  }
  .flyer--front { left: 70px; }
  .flyer--back { left: 630px; }

  .flyer__art { position: absolute; inset: 0; width: 100%; height: 100%; }

  .brand-label {
    position: absolute; top: 28px; left: 115px; width: 270px; height: 84px;
    background: var(--label); border: 3px solid var(--brand-blue);
    display: flex; align-items: center; justify-content: center; gap: 14px;
    transform: rotate(-3deg);
    box-shadow: 0 3px 6px rgba(0,0,0,.3);
  }
  .brand-label__dot { width: 14px; height: 14px; border-radius: 50%; background: var(--logo-ink); flex: none; }
  .brand-label__name {
    font-family: "Arimo", Arial, sans-serif; font-size: 20px; color: var(--logo-ink);
    line-height: 1.2; text-align: center; white-space: nowrap;
  }

  .menu-title {
    position: absolute; top: 126px; left: 0; width: 100%; text-align: center;
    font-family: "Poiret One", sans-serif; font-size: 28px; font-weight: 400; letter-spacing: 4px;
    color: var(--brand-blue-dark);
  }

  .panel {
    position: absolute; top: 190px; width: 218px; height: 410px;
    background: var(--panel); border: 3px solid var(--panel-edge);
    border-radius: 50% 50% 0 0 / 34px 34px 0 0;
    padding: 14px 12px 0;
    font-family: "Arimo", Arial, sans-serif; color: var(--ink);
  }
  .panel--left { left: 24px; }
  .panel--right { left: 258px; }

  .panel__heading {
    font-family: "Cinzel", serif; font-size: 19px; font-weight: 400; text-align: center;
    color: var(--ink); margin-bottom: 8px; letter-spacing: 1px;
  }
  .panel__sub { font-size: 13px; font-weight: 400; margin: 6px 0 2px; }

  .item { display: flex; justify-content: space-between; font-size: 11.2px; line-height: 14.4px; white-space: nowrap; }
  .item__price { flex: none; padding-left: 6px; }
  .gap { height: 9px; }

  .ribbon {
    position: absolute; left: 40px; width: 420px; height: 34px;
    background: var(--brand-blue); color: #fff;
    clip-path: polygon(0 0, 100% 0, 96% 50%, 100% 100%, 0 100%, 4% 50%);
    display: flex; align-items: center; justify-content: center; gap: 10px;
    font-family: "Satisfy", cursive; font-size: 17px; white-space: nowrap;
    transform: rotate(-4deg);
  }
  .ribbon--one { top: 640px; }
  .ribbon--two { top: 690px; left: 60px; }
  .ribbon__dot { width: 6px; height: 6px; border-radius: 50%; background: #fff; flex: none; }

  .disclaimer {
    position: absolute; right: 18px; bottom: 20px;
    font-family: "Arimo", Arial, sans-serif; font-size: 8.5px; color: #fff;
  }
</style>
</head>
<body>
<main class="canvas">

  <section class="flyer flyer--front" aria-label="Menu flyer, front">
    <svg class="flyer__art" viewBox="0 0 500 770">
      <defs>
        <linearGradient id="woodFront" x1="0" y1="0" x2="1" y2="0">
          <stop offset="0" stop-color="#4a2c17"/>
          <stop offset=".5" stop-color="#a06a3c"/>
          <stop offset="1" stop-color="#7a4a26"/>
        </linearGradient>
        <linearGradient id="sunFront" x1="0" y1="0" x2="0" y2="1">
          <stop offset="0" stop-color="#f2a930"/>
          <stop offset=".55" stop-color="#d9781e"/>
          <stop offset="1" stop-color="#2e3d52"/>
        </linearGradient>
      </defs>
      <rect width="500" height="770" fill="url(#woodFront)" role="img" aria-label="Weathered timber boardwalk texture"/>
      <path d="M0 200 Q250 130 500 200 L500 600 Q250 660 0 600 Z" fill="url(#sunFront)" role="img" aria-label="Sunset over the ocean"/>
      <path d="M0 200 Q250 130 500 200 L500 212 Q250 144 0 212 Z" fill="#1d5aa6"/>
      <path d="M0 600 Q250 660 500 600 L500 614 Q250 676 0 614 Z" fill="#1d5aa6"/>
    </svg>

    <div class="brand-label">
      <span class="brand-label__dot"></span>
      <span class="brand-label__name">Red Lantern<br>Take Away</span>
    </div>
    <h1 class="menu-title">MENU</h1>

    <div class="panel panel--left">
      <h2 class="panel__heading">HOT FOOD</h2>
      <div class="item"><span>Minimum Chips</span><span class="item__price">$4.00</span></div>
      <div class="item"><span>Dim Sim - Meat</span><span class="item__price">$1.30</span></div>
      <div class="item"><span>Dim Sim - Veggie</span><span class="item__price">$1.80</span></div>
      <div class="item"><span>Savoury Roll</span><span class="item__price">$2.80</span></div>
      <div class="item"><span>Spring Roll</span><span class="item__price">$1.30</span></div>
      <div class="item"><span>Mini Spring Roll</span><span class="item__price">$3.20</span></div>
      <div class="item"><span>Chicken D/Stick</span><span class="item__price">$1.50</span></div>
      <div class="item"><span>Chicken Wing Ding</span><span class="item__price">$2.20</span></div>
      <div class="item"><span>Chicken Strips</span><span class="item__price">$1.80</span></div>
      <div class="item"><span>Pineapple Fritter</span><span class="item__price">$0.80</span></div>
      <div class="item"><span>Chicken Nuggets</span><span class="item__price">$2.60</span></div>
      <div class="item"><span>Corn Bites</span><span class="item__price">$0.90</span></div>
      <div class="item"><span>Corn Fritter</span><span class="item__price">$2.50</span></div>
      <div class="item"><span>Chicken Corn Roll</span><span class="item__price">$2.50</span></div>
      <div class="item"><span>Beef Croquets</span><span class="item__price">$1.30</span></div>
      <div class="item"><span>Chicken Garlic Balls</span><span class="item__price">$1.40</span></div>
      <div class="item"><span>Potato Scallops</span><span class="item__price">$0.95</span></div>
      <div class="item"><span>Potato Gems</span><span class="item__price">$1.90</span></div>
      <div class="item"><span>Battered Sav</span><span class="item__price">$2.60</span></div>
    </div>

    <div class="panel panel--right">
      <h2 class="panel__heading">BURGERS</h2>
      <div class="item"><span>Hamburger - Plain</span><span class="item__price">$6.50</span></div>
      <div class="item"><span>Hamburger - Egg</span><span class="item__price">$7.50</span></div>
      <div class="item"><span>Hamburger - Lot</span><span class="item__price">$8.50</span></div>
      <div class="item"><span>Cheese Burger</span><span class="item__price">$6.50</span></div>
      <div class="item"><span>Chicken Schnitzel - Plain</span><span class="item__price">$7.50</span></div>
      <div class="item"><span>Chicken Schnitzel - Lot</span><span class="item__price">$9.00</span></div>
      <div class="item"><span>Grilled Fish Burger</span><span class="item__price">$8.00</span></div>
      <div class="item"><span>Battered Fish Burger</span><span class="item__price">$6.00</span></div>
      <div class="item"><span>Prawn Burger</span><span class="item__price">$8.00</span></div>
      <div class="item"><span>Scallop Burger - Plain</span><span class="item__price">$7.00</span></div>
      <div class="item"><span>Scallop Burger - Lot</span><span class="item__price">$9.00</span></div>
      <div class="item"><span>Steak Sandwich - Plain</span><span class="item__price">$7.50</span></div>
      <div class="item"><span>Steak Sandwich - Lot</span><span class="item__price">$9.00</span></div>
      <div class="item"><span>Bacon &amp; Egg Roll</span><span class="item__price">$6.50</span></div>
      <h3 class="panel__sub">Extras</h3>
      <div class="item"><span>Pineapple</span><span class="item__price">$0.50</span></div>
      <div class="item"><span>Cheese</span><span class="item__price">$0.50</span></div>
      <div class="item"><span>Egg</span><span class="item__price">$0.50</span></div>
      <div class="item"><span>Bacon</span><span class="item__price">$1.00</span></div>
      <div class="item"><span>Salad (Lettuce, Tomato,<br>Beetroot - each)</span><span class="item__price">$0.50</span></div>
    </div>

    <div class="ribbon ribbon--one"><span>14 Lantern St</span><span class="ribbon__dot"></span><span>02 6900 1234</span></div>
    <div class="ribbon ribbon--two"><span>Shop 12 Riverside Plaza</span><span class="ribbon__dot"></span><span>02 6900 5678</span></div>
    <p class="disclaimer">Please note: Prices may be subject to change</p>
  </section>

  <section class="flyer flyer--back" aria-label="Menu flyer, back">
    <svg class="flyer__art" viewBox="0 0 500 770">
      <defs>
        <linearGradient id="woodBack" x1="0" y1="0" x2="1" y2="0">
          <stop offset="0" stop-color="#7a4a26"/>
          <stop offset=".5" stop-color="#a06a3c"/>
          <stop offset="1" stop-color="#4a2c17"/>
        </linearGradient>
        <linearGradient id="sunBack" x1="0" y1="0" x2="0" y2="1">
          <stop offset="0" stop-color="#f2a930"/>
          <stop offset=".55" stop-color="#d9781e"/>
          <stop offset="1" stop-color="#2e3d52"/>
        </linearGradient>
      </defs>
      <rect width="500" height="770" fill="url(#woodBack)" role="img" aria-label="Weathered timber boardwalk texture"/>
      <path d="M0 200 Q250 130 500 200 L500 600 Q250 660 0 600 Z" fill="url(#sunBack)" role="img" aria-label="Sunset over the ocean"/>
      <path d="M0 200 Q250 130 500 200 L500 212 Q250 144 0 212 Z" fill="#1d5aa6"/>
      <path d="M0 600 Q250 660 500 600 L500 614 Q250 676 0 614 Z" fill="#1d5aa6"/>
    </svg>

    <div class="brand-label">
      <span class="brand-label__dot"></span>
      <span class="brand-label__name">Red Lantern<br>Take Away</span>
    </div>
    <h2 class="menu-title">MENU</h2>

    <div class="panel panel--left">
      <h2 class="panel__heading">SEAFOOD</h2>
      <div class="item"><span>Fish - Battered</span><span class="item__price">$7.00</span></div>
      <div class="item"><span>Fish - Grilled</span><span class="item__price">$7.50</span></div>
      <div class="item"><span>Fish - Crumbed</span><span class="item__price">$7.50</span></div>
      <div class="item"><span>Fish - Cocktail</span><span class="item__price">$1.40</span></div>
      <div class="item"><span>Barramundi</span><span class="item__price">$8.00</span></div>
      <div class="gap"></div>
      <div class="item"><span>Grilled Fish &amp; Chips</span><span class="item__price">$9.50</span></div>
      <div class="item"><span>Grilled Fish, Salad &amp; Chips</span><span class="item__price">$12.50</span></div>
      <div class="item"><span>Barramundi &amp; Chips</span><span class="item__price">$10.00</span></div>
      <div class="item"><span>Barramundi &amp; Salad</span><span class="item__price">$11.00</span></div>
      <div class="item"><span>Barramundi, Salad &amp; Chips</span><span class="item__price">$13.00</span></div>
      <div class="gap"></div>
      <div class="item"><span>Seafood Basket</span><span class="item__price">$11.00</span></div>
      <div class="item"><span>Fish Cake</span><span class="item__price">$3.00</span></div>
      <div class="item"><span>Prawn Cutlet</span><span class="item__price">$2.30</span></div>
      <div class="item"><span>Tassie Scallop</span><span class="item__price">$1.80</span></div>
      <div class="item"><span>Calamari Rings</span><span class="item__price">$1.30</span></div>
      <div class="item"><span>Sea Shanties</span><span class="item__price">$1.30</span></div>
      <div class="item"><span>Prawn Bar</span><span class="item__price">$2.60</span></div>
      <div class="item"><span>Seafood Stick</span><span class="item__price">$2.40</span></div>
    </div>

    <div class="panel panel--right">
      <h2 class="panel__heading">SANDWICHES</h2>
      <h3 class="panel__sub">Toasted</h3>
      <div class="item"><span>Cheese</span><span class="item__price">$3.00</span></div>
      <div class="item"><span>Cheese &amp; Tomato</span><span class="item__price">$3.50</span></div>
      <div class="item"><span>Ham &amp; Cheese</span><span class="item__price">$4.50</span></div>
      <div class="item"><span>Ham, Cheese &amp; Tomato</span><span class="item__price">$5.00</span></div>
      <h3 class="panel__sub">Fresh</h3>
      <div class="item"><span>Cheese</span><span class="item__price">$2.50</span></div>
      <div class="item"><span>Cheese &amp; Tomato</span><span class="item__price">$3.00</span></div>
      <div class="item"><span>Ham &amp; Cheese</span><span class="item__price">$4.00</span></div>
      <div class="item"><span>Salad (inc. Cheese &amp; Mayo)</span><span class="item__price">$4.50</span></div>
      <div class="item"><span>Ham, Cheese &amp; Salad<br>(inc. Mayo)</span><span class="item__price">$5.50</span></div>
      <h3 class="panel__sub">Rolls</h3>
      <div class="item"><span>Salad<br>(inc. Cheese &amp; Mayo)</span><span class="item__price">$5.00</span></div>
      <div class="item"><span>Ham, Cheese &amp; Salad<br>(inc. Mayo)</span><span class="item__price">$6.00</span></div>
    </div>

    <div class="ribbon ribbon--one"><span class="ribbon__dot"></span><span>Find us online: Red Lantern Take Away</span><span class="ribbon__dot"></span></div>
    <div class="ribbon ribbon--two"><span class="ribbon__dot"></span><span>www.redlanterntakeaway.com</span><span class="ribbon__dot"></span></div>
    <p class="disclaimer">Please note: Prices may be subject to change</p>
  </section>

</main>
</body>
</html>
```